Construction company looking for modern

**Tallow Crest Joinery Limited**

We need a website for a renovation/remodeling company based in Hamilton, New Zealand. Ideally it will catch clients' attention and be modern and professional looking. I have attached a logo that I have just recently had made (through PixelHarbor). If the website could reflect this style and colour schemes, that would be awesome. The final design should communicate a trustworthiness and professionalism.

I have attached photos of a website that I really think is great, so if we could have something that follows along those likes,

https://www.dailyplover.example/local-news/news/local-builder-named-top-apprentice-for-region/QZTRPLA8VXN2MJ5DFYUEKHSWGO/

I won a competition a few years ago while I was an apprentice, If we could somehow put that in there as one of my achievements to try to bring in some trust that would be awesome. I would like to add a new picture though because my beard in that photo is wild.

Target Market(s)

Families that want live in the homes that i'm working on. not investors. People that are looking for quality not cheapest price.

Industry/Entity Type

Construction, Home renovations, Maintenance, Deck Builds, New Builds, Bathrooms, Kitchens

Coding

Coded - Design and coding required

Number of Pages Required

5+ page

Font styles to use
Sans Serif

Colors
6B429C
8869AF
B7A5CE
E3DAEB
F3F0F8

Requirements
Must have
• Contact us page, large clear pictures, Colours the work with the purple in my logo. That will be my company colour so I'm thinking black and purple, or what ever compliments purple nicely
Nice to have
• Page for Renovations, Testimonials, Contact us, Home, About us
Should not have
• Plain looking pages, empty white space, I want the text to be beside a nice big picture etc

```html
<!DOCTYPE html>
<html lang="en">
<head>
<meta charset="utf-8">
<title>Tallow Crest Joinery Ltd</title>
<link href="https://fonts.googleapis.com/css2?family=Poppins:wght@300;400;500;600;700&family=Montserrat:wght@600;700&display=swap" rel="stylesheet">
<style>
:root{
  --purple:#6b3a9c;
  --purple-mid:#8869af;
  --purple-soft:#b7a5ce;
  --lilac:#e3daeb;
  --dark:#3d3d3f;
  --darker:#343436;
  --grey:#f3f3f3;
  --text:#444;
  --white:#fff;
  --gold:#f4b400;
}
*{box-sizing:border-box;margin:0;padding:0}
html,body{width:1200px;height:4764px;overflow:hidden}
body{font-family:"Poppins",sans-serif;color:var(--text);background:var(--white);position:relative}
.abs{position:absolute}
.btn{position:absolute;display:flex;align-items:center;justify-content:center;font-size:10px;font-weight:600;text-transform:uppercase;color:var(--white);letter-spacing:.2px}
.btn-purple{background:var(--purple)}
.btn-dark{background:var(--dark)}
.brand{font-family:"Poppins",sans-serif;font-weight:600;color:var(--purple);display:flex;align-items:center;gap:6px;line-height:1.1}
.brand .mark{width:12px;height:12px;background:var(--purple);flex:none}
.photo{position:absolute}
.center{text-align:center}
.sec-title{position:absolute;left:0;width:1200px;text-align:center;font-size:29px;font-weight:400;color:var(--dark)}
.sec-title b{font-weight:600}
.sec-title span{color:var(--purple)}
.sec-lead{position:absolute;left:240px;width:720px;text-align:center;font-size:13.5px;line-height:25px;color:var(--text)}

/* header */
.nav{position:absolute;top:66px;font-size:11px;color:var(--text);text-transform:uppercase}
.nav.active{color:var(--purple)}
.phone{position:absolute;left:923px;top:16px;width:133px;height:32px;background:var(--dark);display:flex;align-items:center;color:var(--white);font-size:11px}
.phone .ico{width:32px;height:32px;background:var(--purple);display:flex;align-items:center;justify-content:center;margin-right:10px}

/* hero */
.hero-left{left:0;top:114px;width:610px;height:495px;background:var(--dark)}
.hero-title{left:141px;top:266px;font-family:"Montserrat",sans-serif;font-weight:700;font-size:50px;color:var(--white);letter-spacing:.5px}
.hero-sub{left:142px;top:326px;font-size:22px;color:var(--white);letter-spacing:5px}
.hero-text{left:142px;top:364px;width:400px;font-size:14px;line-height:23px;color:#cfcfcf}

/* band */
.band-title{font-size:17px;font-weight:600;color:var(--white)}
.band-text{font-size:14px;color:#e6def0;margin-top:3px}

/* cards */
.card{position:absolute;top:1459px;width:291px;height:359px;background:var(--grey)}
.card.featured{background:var(--purple)}
.card h3{position:absolute;top:208px;left:0;width:100%;text-align:center;font-size:17px;font-weight:500;color:var(--purple);text-transform:uppercase}
.card.featured h3{color:var(--white)}
.card p{position:absolute;top:243px;left:45px;width:201px;text-align:center;font-size:10.5px;line-height:18px;color:var(--text)}
.card.featured p{color:#eee}
.card .btn{top:346px;left:96px;width:100px;height:25px;font-size:9px}

/* tabs */
.tab{position:absolute;top:2609px;width:202px;height:120px;background:#f0f0f0;text-align:center;color:var(--purple);font-size:19px}
.tab.active{background:var(--dark);color:var(--white)}
.tab svg{display:block;margin:30px auto 8px}

/* testimonials */
.tcard{position:absolute;top:3655px;width:291px;height:255px;background:var(--white);box-shadow:0 2px 14px rgba(0,0,0,.09)}
.stars{position:absolute;left:25px;top:30px;color:var(--gold);font-size:16px;letter-spacing:0}
.tcard p{position:absolute;left:25px;top:65px;width:245px;font-size:10px;line-height:17px;color:#777}
.who{position:absolute;left:25px;top:198px;display:flex;align-items:center;gap:10px}
.avatar{width:32px;height:32px;border-radius:50%;background:linear-gradient(135deg,#b79e87,#5e5048)}
.who b{display:block;font-size:11px;color:var(--purple);font-weight:600}
.who small{display:block;font-size:9px;color:var(--purple-mid)}

/* contact */
.field-label{position:absolute;font-size:10px;color:#eee}
.field-line{position:absolute;height:1px;background:#c9b8de}

/* footer */
.f-head{position:absolute;top:4488px;font-size:17px;font-weight:500;color:var(--white)}
.f-list{position:absolute;top:4520px;list-style:none;font-size:10px;color:#ddd;line-height:22px}
</style>
</head>
<body>

<!-- header -->
<header>
  <div class="abs brand" style="left:146px;top:40px;font-size:15px;width:130px"><span class="mark"></span>Tallow Crest Joinery Ltd</div>
  <div class="phone"><span class="ico"><svg width="14" height="14" viewBox="0 0 24 24" fill="none" stroke="#fff" stroke-width="2"><path d="M5 3h4l2 5-3 2a11 11 0 0 0 6 6l2-3 5 2v4a2 2 0 0 1-2 2A18 18 0 0 1 3 5a2 2 0 0 1 2-2z"/></svg></span>021-555-0148</div>
  <nav>
    <div class="nav active" style="left:483px">Home</div>
    <div class="nav" style="left:575px">About Us</div>
    <div class="nav" style="left:692px">Renovations</div>
    <div class="nav" style="left:837px">Testimonials</div>
    <div class="nav" style="left:978px">Contact Us</div>
  </nav>
</header>

<!-- hero -->
<section>
  <div class="abs hero-left"></div>
  <div class="photo" role="img" aria-label="Carpenter's hands working on timber boards with hammer, drill and tool case" style="left:610px;top:114px;width:590px;height:495px;background:linear-gradient(135deg,#d9c3a4 0%,#b89369 45%,#6f5a49 100%)"></div>
  <div class="abs hero-title">TALLOW CREST</div>
  <div class="abs hero-sub">JOINERY LTD</div>
  <div class="abs hero-text">Renovation/Remodeling Company Based In Hamilton, New Zealand</div>
  <div class="btn btn-purple" style="left:143px;top:438px;width:110px;height:32px">Read More</div>
</section>

<!-- quality band -->
<section>
  <svg class="abs" style="left:0;top:609px" width="1200" height="110"><rect width="1200" height="110" fill="#3d3d3f"/><polygon points="0,0 635,0 565,110 0,110" fill="#6b3a9c"/><line x1="635" y1="0" x2="565" y2="110" stroke="#fff" stroke-width="2"/></svg>
  <svg class="abs" style="left:145px;top:640px" width="40" height="46" viewBox="0 0 40 46" fill="none" stroke="#fff" stroke-width="2"><path d="M20 2 36 8v14c0 11-7 18-16 22C11 40 4 33 4 22V8z"/><path d="M12 23l6 6 11-12"/></svg>
  <div class="abs" style="left:203px;top:640px"><div class="band-title">BEST QUALITY</div><div class="band-text">Lorem Ipsum Dolor Sit Amet</div></div>
  <div class="btn btn-dark" style="left:462px;top:652px;width:88px;height:32px">Get A Quote</div>
  <svg class="abs" style="left:640px;top:644px" width="44" height="40" viewBox="0 0 44 40" fill="none" stroke="#fff" stroke-width="2"><rect x="8" y="2" width="34" height="24" rx="2"/><path d="M2 12v20h8v6l6-6h14"/><path d="M29 8h-6a3 3 0 0 0 0 6h2a3 3 0 0 1 0 6h-6M24 5v18"/></svg>
  <div class="abs" style="left:703px;top:640px"><div class="band-title">QUOTE REQUEST</div><div class="band-text" style="color:#cfcfcf">Renovation And Remodeling</div></div>
  <div class="btn btn-purple" style="left:965px;top:652px;width:90px;height:32px">Get A Quote</div>
</section>

<!-- about -->
<section>
  <div class="abs" style="left:120px;top:822px;width:282px;height:218px;background:var(--purple)"></div>
  <div class="abs" style="left:270px;top:1020px;width:282px;height:163px;background:var(--dark)"></div>
  <div class="photo" role="img" aria-label="Tradesman in hard hat and checked shirt working at a machine in a workshop" style="left:143px;top:845px;width:385px;height:315px;background:linear-gradient(135deg,#8a5a3c 0%,#4f3a33 50%,#2e2a2c 100%)"></div>
  <div class="abs" style="left:600px;top:853px;height:27px;padding:0 12px;background:var(--purple);color:var(--white);font-size:13.5px;font-weight:500;display:flex;align-items:center">Renovation and Remodeling Solutions</div>
  <h2 class="abs" style="left:600px;top:902px;font-size:31px;font-weight:500;color:var(--dark)">About Tallow Crest</h2>
  <p class="abs" style="left:600px;top:953px;width:460px;font-size:13.5px;line-height:25px">Lorem Ipsum is simply dummy text of the printing and typesetting industry. Lorem Ipsum has been the industry's standard dummy text ever since the 1500s, when an unknown printer took a galley of type and scrambled it to make a type specimen book. It has survived not only five centuries</p>
  <div class="btn btn-purple" style="left:600px;top:1117px;width:93px;height:31px">Learn More</div>
</section>

<!-- renovations -->
<section>
  <h2 class="sec-title" style="top:1308px"><span>OUR</span> <b>RENOVATIONS</b></h2>
  <p class="sec-lead" style="top:1361px">Lorem Ipsum is simply dummy text of the printing and typesetting industry. Lorem Ipsum has been the industry's standard dummy text ever since the 1500s, when an unknown.</p>
  <div class="card" style="left:145px">
    <div class="photo" role="img" aria-label="Plumber fitting a modern bathroom" style="left:0;top:0;width:291px;height:192px;background:linear-gradient(135deg,#9a9894,#5d5a57 60%,#3e6b8e)"></div>
    <h3>Bathrooms</h3><p>Lorem ipsum is simply dummy text of the printing and typesetting industry. Lorem Ipsum.</p>
    <div class="btn btn-dark">Service Detail</div>
  </div>
  <div class="card featured" style="left:455px">
    <div class="photo" role="img" aria-label="Bright kitchen with light timber cabinets" style="left:0;top:0;width:291px;height:192px;background:linear-gradient(135deg,#e6dccb,#cbb79a 55%,#7c7770)"></div>
    <h3>Kitchen</h3><p>Lorem ipsum is simply dummy text of the printing and typesetting industry. Lorem Ipsum.</p>
    <div class="btn btn-dark">Service Detail</div>
  </div>
  <div class="card" style="left:765px">
    <div class="photo" role="img" aria-label="Gloved hands hammering deck boards" style="left:0;top:0;width:291px;height:192px;background:linear-gradient(135deg,#3b2418,#a0612e 55%,#d39a5c)"></div>
    <h3>Deck Builds</h3><p>Lorem ipsum is simply dummy text of the printing and typesetting industry. Lorem Ipsum.</p>
    <div class="btn btn-dark">Service Detail</div>
  </div>
  <svg class="abs" style="left:566px;top:1904px" width="70" height="29"><circle cx="14" cy="14.5" r="14" fill="#3d3d3f"/><path d="M17 9l-6 5.5 6 5.5" stroke="#fff" stroke-width="2.2" fill="none"/><circle cx="56" cy="14.5" r="14" fill="#6b3a9c"/><path d="M53 9l6 5.5-6 5.5" stroke="#fff" stroke-width="2.2" fill="none"/></svg>
</section>

<!-- recent projects -->
<section>
  <div class="abs" style="left:0;top:2005px;width:1200px;height:260px;background:var(--dark)"></div>
  <h2 class="sec-title" style="top:2090px;color:var(--white)">RECENT <b>PROJECTS</b></h2>
  <p class="sec-lead" style="top:2141px;color:var(--white)">Lorem Ipsum is simply dummy text of the printing and typesetting industry. Lorem Ipsum has been the industry's standard dummy text ever since the 1500s, when an unknown.</p>
  <div class="photo" role="img" aria-label="Finished renovated interior" style="left:0;top:2265px;width:300px;height:199px;background:linear-gradient(135deg,#8d8a86,#c7c1b8)"></div>
  <div class="photo" role="img" aria-label="Saw cutting timber with flying sawdust" style="left:300px;top:2265px;width:300px;height:199px;background:linear-gradient(135deg,#1f1713,#5c3b26 60%,#8a5a34)"></div>
  <div class="photo" role="img" aria-label="Timber roof framing under construction" style="left:600px;top:2265px;width:300px;height:199px;background:linear-gradient(135deg,#7a5030,#b9855a 55%,#d6b48c)"></div>
  <div class="photo" role="img" aria-label="Carpenter measuring timber on site" style="left:900px;top:2265px;width:300px;height:199px;background:linear-gradient(135deg,#c7a988,#8b6b52 60%,#5c4a3e)"></div>
  <div class="btn btn-purple" style="left:100px;top:2358px;width:100px;height:28px;font-size:9px">View Projects</div>
  <div class="btn" style="left:700px;top:2358px;width:100px;height:28px;font-size:9px;border:1px solid #fff">View Projects</div>
  <div class="btn" style="left:1000px;top:2358px;width:100px;height:28px;font-size:9px;border:1px solid #fff">View Projects</div>
  <div class="abs" style="left:0;top:2464px;width:1200px;height:97px;background:var(--purple)"></div>
  <div class="abs" style="left:397px;top:2500px;font-size:17px;font-weight:600;color:var(--white)">DISCOVER OUR INITIATIVES</div>
  <div class="btn btn-dark" style="left:676px;top:2498px;width:127px;height:30px;font-size:9px">View All Projects</div>
</section>

<!-- offer tabs -->
<section>
  <div class="tab active" style="left:280px"><svg width="30" height="28" viewBox="0 0 30 28" fill="none" stroke="#fff" stroke-width="1.6"><rect x="4" y="2" width="22" height="24" rx="2"/><path d="M9 9h12M9 14h12M9 19h7"/></svg>We Offer</div>
  <svg class="abs" style="left:371px;top:2729px" width="20" height="10"><polygon points="0,0 20,0 10,10" fill="#3d3d3f"/></svg>
  <div class="tab" style="left:500px"><svg width="30" height="28" viewBox="0 0 30 28" fill="none" stroke="#6b3a9c" stroke-width="1.6"><path d="M15 2l10 4v8c0 6-4 10-10 12C9 24 5 20 5 14V6z"/><path d="M10 14l4 4 7-8"/></svg>We Guarantee</div>
  <div class="tab" style="left:719px"><svg width="34" height="28" viewBox="0 0 34 28" fill="none" stroke="#6b3a9c" stroke-width="1.6"><rect x="2" y="5" width="18" height="14"/><path d="M20 9h7l5 5v5H20"/><circle cx="8" cy="21" r="3"/><circle cx="26" cy="21" r="3"/></svg>We Provide</div>
  <h2 class="abs center" style="left:0;top:2791px;width:1200px;font-size:19px;font-weight:400;color:var(--dark)">OUR <span style="color:var(--purple);font-weight:600">OFFER</span></h2>
  <p class="sec-lead" style="top:2829px">Lorem Ipsum is simply dummy text of the printing and typesetting industry. Lorem Ipsum has been the industry's standard dummy text ever since the 1500s, when an unknown.</p>
</section>

<!-- who we are -->
<section>
  <svg class="abs" style="left:0;top:2975px" width="1200" height="381"><rect width="1200" height="381" fill="#f0f0f0"/><polygon points="0,0 1000,0 1000,381 325,381" fill="#6b3a9c"/></svg>
  <div class="abs" style="left:940px;top:2920px;width:184px;height:184px;border-radius:50%;background:var(--dark)"></div>
  <div class="abs" style="left:840px;top:3230px;width:180px;height:180px;border-radius:50%;background:var(--white)"></div>
  <div class="photo" role="img" aria-label="Smiling bearded tradesman in overalls with arms crossed" style="left:890px;top:2955px;width:290px;height:401px;border-radius:145px 145px 0 0;background:linear-gradient(180deg,#6e5446 0%,#b7a394 45%,#8a8a8a 100%)"></div>
  <div class="abs brand" style="left:36px;top:3240px;font-size:14px;width:120px"><span class="mark"></span>Tallow Crest Joinery Ltd</div>
  <h2 class="abs" style="left:330px;top:3030px;font-size:30px;font-weight:600;color:var(--white)">Who We Are</h2>
  <p class="abs" style="left:332px;top:3084px;width:520px;font-size:13.5px;line-height:25px;color:var(--white)">Lorem Ipsum is simply dummy text of the printing and typesetting industry. Lorem Ipsum has been the industry's standard dummy text ever since the 1500s, when an unknown.</p>
  <p class="abs" style="left:332px;top:3171px;width:520px;font-size:13.5px;line-height:25px;color:var(--white)">Lorem Ipsum is simply dummy text of the printing and typesetting industry. Lorem Ipsum has been the industry's standard dummy text ever.</p>
  <div class="btn btn-dark" style="left:335px;top:3258px;width:104px;height:26px;font-size:9px;text-transform:none">View More</div>
</section>

<!-- testimonials -->
<section>
  <h2 class="sec-title" style="top:3485px"><span>OUR</span> <b style="color:var(--purple)">TESTIMONIALS</b></h2>
  <p class="sec-lead" style="top:3538px">Lorem Ipsum is simply dummy text of the printing and typesetting industry. Lorem Ipsum has been the industry's standard dummy text ever since the 1500s, when an unknown.</p>
  <div class="tcard" style="left:145px"><div class="stars">★★★★★</div><p>"Working With Corin Was A Game-Changer For Our Company. His Strategic Insights And Personalized Coaching Transformed The Way We Approach Business. With His Guidance, We've Seen Significant Growth And Improved Team Dynamics."</p><div class="who"><span class="avatar"></span><div><b>Aaron Welby</b><small>CEO Of Northfield Systems Ltd</small></div></div></div>
  <div class="tcard" style="left:455px"><div class="stars">★★★★★</div><p>"I Can't Recommend Corin's Coaching Enough! His Practical Advice And Genuine Support Have Been Instrumental In My Entrepreneurial Journey. He Helped Me Overcome Challenges And Gave Me The Confidence To Take My Business To New Heights"</p><div class="who"><span class="avatar"></span><div><b>Hana Lorimer</b><small>Entrepreneur And Founder</small></div></div></div>
  <div class="tcard" style="left:765px"><div class="stars">★★★★★</div><p>"Corin's Marketing Expertise Has Been Invaluable To Our Team. His Creative Strategies And Deep Industry Knowledge Have Helped Us Develop Impactful Campaigns That Resonate With Our Target Audience. Our Marketing Effort."</p><div class="who"><span class="avatar"></span><div><b>Rawiri Kent</b><small>Marketing Manager At Brightline Studio</small></div></div></div>
</section>

<!-- contact -->
<section>
  <div class="abs" style="left:0;top:4031px;width:410px;height:389px;background:#f3f3f3"></div>
  <div class="abs" style="left:410px;top:4031px;width:790px;height:389px;background:var(--purple)"></div>
  <div class="abs brand" style="left:146px;top:4120px;font-size:17px;width:150px"><span class="mark"></span>Tallow Crest Joinery Ltd</div>
  <svg class="abs" style="left:143px;top:4238px" width="12" height="16" viewBox="0 0 12 16" fill="none" stroke="#6b3a9c" stroke-width="1.5"><path d="M6 15s5-5 5-9A5 5 0 0 0 1 6c0 4 5 9 5 9z"/><circle cx="6" cy="6" r="1.8"/></svg>
  <div class="abs" style="left:169px;top:4234px;font-size:13px;color:var(--purple)">Location</div>
  <div class="abs" style="left:169px;top:4253px;width:160px;font-size:9.5px;line-height:14px;color:#888">18 Kowhai Lane, Hamilton 3204, New Zealand</div>
  <svg class="abs" style="left:143px;top:4306px" width="14" height="14" viewBox="0 0 24 24" fill="none" stroke="#6b3a9c" stroke-width="2"><path d="M5 3h4l2 5-3 2a11 11 0 0 0 6 6l2-3 5 2v4a2 2 0 0 1-2 2A18 18 0 0 1 3 5a2 2 0 0 1 2-2z"/></svg>
  <div class="abs" style="left:169px;top:4304px;font-size:13px;color:var(--purple)">Contact Us</div>
  <div class="abs" style="left:169px;top:4323px;font-size:9.5px;color:#888">07-555-0192</div>

  <h2 class="abs" style="left:467px;top:4084px;font-size:17px;font-weight:600;letter-spacing:2.6px;color:var(--white)">FOR ANY QUESTIONS SEND US A MESSAGE</h2>
  <div class="field-label" style="left:467px;top:4138px">First Name*</div>
  <div class="field-line" style="left:467px;top:4167px;width:283px"></div>
  <div class="field-label" style="left:772px;top:4138px">Your Message</div>
  <div class="field-label" style="left:467px;top:4196px">Last Name*</div>
  <div class="field-line" style="left:467px;top:4224px;width:283px"></div>
  <div class="field-label" style="left:467px;top:4255px">Email Address</div>
  <div class="field-line" style="left:467px;top:4283px;width:283px"></div>
  <div class="field-line" style="left:772px;top:4283px;width:284px"></div>
  <div class="btn btn-dark" style="left:928px;top:4322px;width:128px;height:33px;font-size:11px">Submit</div>
</section>

<!-- footer -->
<footer>
  <div class="abs" style="left:0;top:4420px;width:1200px;height:344px;background:var(--dark)"></div>
  <div class="abs" style="left:137px;top:4487px;width:153px;height:118px;background:var(--white)"></div>
  <div class="abs brand" style="left:152px;top:4530px;font-size:15px;width:130px"><span class="mark"></span>Tallow Crest Joinery Ltd</div>
  <div class="f-head" style="left:378px">Our Company</div>
  <ul class="f-list" style="left:378px"><li>Home</li><li>About Us</li><li>Renovations</li><li>Testimonials</li><li>Contact Us</li></ul>
  <div class="f-head" style="left:591px">Partner With Us</div>
  <ul class="f-list" style="left:591px"><li>Privacy Policies</li><li>Term and Conditions</li><li>Term and Services</li></ul>
  <div class="f-head" style="left:822px">Contact Us</div>
  <svg class="abs" style="left:822px;top:4519px" width="12" height="10" viewBox="0 0 12 10" fill="none" stroke="#ddd" stroke-width="1.2"><rect x=".6" y=".6" width="10.8" height="8.8"/><path d="M1 1l5 4 5-4"/></svg>
  <div class="abs" style="left:844px;top:4516px;font-size:10px;color:#ddd">hello@tallowcrest.example</div>
  <svg class="abs" style="left:823px;top:4540px" width="10" height="13" viewBox="0 0 12 16" fill="none" stroke="#ddd" stroke-width="1.5"><path d="M6 15s5-5 5-9A5 5 0 0 0 1 6c0 4 5 9 5 9z"/><circle cx="6" cy="6" r="1.8"/></svg>
  <div class="abs" style="left:844px;top:4538px;font-size:10px;color:#ddd">Hamilton East 3216</div>
  <svg class="abs" style="left:822px;top:4576px" width="78" height="22"><circle cx="11" cy="11" r="10" fill="#6b3a9c"/><circle cx="37" cy="11" r="10" fill="none" stroke="#ddd"/><circle cx="63" cy="11" r="10" fill="none" stroke="#ddd"/></svg>
  <div class="abs" style="left:0;top:4730px;width:1200px;text-align:center;font-size:10px;color:#ccc">Copyright © 2023 tallowcrest.example. All rights Reserved.</div>
</footer>

</body>
</html>
```